Business Card Design needed for logo design project

This project is linked to a href='http://jobs.plankforge.net/job.aspx?id=417902'Keel Drift: Design a logo for our new trailer boat syndication business in Sydney
Our company needs a Business Card Design. Please refer to our original project in the link above.
I would like a relatively simple and classy business card design. could you please also use small symbols for identifying contact info eg. mobile, web and email?
Updates
Please see my new project to design a business card for a trailer boat syndication business in Sydney, Australia.
Industry/Entity Type
Business
Look and feel
Each slider illustrates characteristics of the customer's brand and the style your logo design should communicate.

```html
<!DOCTYPE html>
<html lang="en">
<head>
<meta charset="utf-8">
<title>Keel Drift – Business Cards</title>
<link href="https://fonts.googleapis.com/css2?family=Open+Sans:wght@400;600;700;800&display=swap" rel="stylesheet">
<style>
  :root {
    --teal: #2aacb6;
    --teal-dark: #1f97a0;
    --ink: #2b2b2b;
    --rule: #3a3a3a;
    --paper: #ffffff;
    --backdrop: #e6e8e9;
  }
  * { margin: 0; padding: 0; box-sizing: border-box; }
  html, body {
    width: 1200px; height: 676px; overflow: hidden;
    background: var(--backdrop);
    font-family: "Open Sans", Arial, sans-serif;
  }
  .stage {
    position: relative; width: 1200px; height: 676px;
    display: flex; align-items: center; justify-content: center; gap: 40px;
  }
  .card {
    position: relative; width: 500px; height: 286px;
    box-shadow: 0 6px 18px rgba(0,0,0,.18);
    overflow: hidden;
  }

  /* front */
  .card-front { background: var(--teal); display: flex; align-items: center; justify-content: center; }
  .brand { display: flex; flex-direction: column; align-items: center; gap: 6px; }
  .brand-row { display: flex; align-items: center; gap: 12px; }
  .brand-dot { width: 18px; height: 18px; border-radius: 50%; }
  .brand-name { font-weight: 800; font-size: 44px; letter-spacing: .5px; line-height: 1; }
  .brand-tagline { font-size: 9px; letter-spacing: 1.4px; text-transform: uppercase; font-weight: 600; }
  .card-front .brand-dot { background: var(--paper); }
  .card-front .brand-name { color: var(--paper); }
  .card-front .brand-tagline { color: var(--paper); }

  /* back */
  .card-back { background: var(--paper); }
  .back-top { position: absolute; left: 0; top: 0; width: 100%; height: 188px; }
  .back-rule { position: absolute; left: 0; top: 188px; width: 100%; height: 6px; background: var(--rule); }
  .back-band { position: absolute; left: 0; top: 194px; width: 100%; height: 92px; background: var(--teal); }

  .back-brand { position: absolute; left: 34px; top: 68px; }
  .back-brand .brand-row { gap: 8px; }
  .back-brand .brand-dot { width: 12px; height: 12px; background: var(--teal); }
  .back-brand .brand-name { font-size: 30px; color: var(--teal); }
  .back-brand .brand-tagline { font-size: 6.5px; color: var(--ink); letter-spacing: 1px; }

  .divider { position: absolute; left: 248px; top: 34px; width: 1px; height: 132px; background: #9aa0a3; }

  .contact { position: absolute; left: 266px; top: 44px; list-style: none; font-size: 12.5px; color: var(--ink); }
  .contact li { display: flex; align-items: flex-start; gap: 10px; margin-bottom: 5px; line-height: 1.25; }
  .contact li.address { color: var(--teal); margin-bottom: 8px; }
  .contact svg { flex: 0 0 12px; width: 12px; height: 12px; margin-top: 2px; fill: none; stroke: var(--teal); stroke-width: 1.6; }
  .contact .solid { fill: var(--teal); stroke: none; }

  .holder { position: absolute; left: 0; top: 206px; width: 240px; text-align: center; color: var(--paper); }
  .holder-name { font-size: 20px; line-height: 1.2; }
  .holder-role { font-size: 12px; }
</style>
</head>
<body>
<main class="stage">

  <section class="card card-front" aria-label="Card front">
    <div class="brand">
      <div class="brand-row">
        <span class="brand-dot"></span>
        <span class="brand-name">Keel Drift</span>
      </div>
      <span class="brand-tagline">trailer boat syndication and management</span>
    </div>
  </section>

  <section class="card card-back" aria-label="Card back">
    <div class="back-top"></div>
    <div class="back-rule"></div>
    <div class="back-band"></div>

    <div class="brand back-brand">
      <div class="brand-row">
        <span class="brand-dot"></span>
        <span class="brand-name">Keel Drift</span>
      </div>
      <span class="brand-tagline">trailer boat syndication and management</span>
    </div>

    <div class="divider"></div>

    <ul class="contact">
      <li class="address">
        <svg viewBox="0 0 12 12"><path class="solid" d="M6 0.5a4 4 0 0 0-4 4c0 3 4 7 4 7s4-4 4-7a4 4 0 0 0-4-4zm0 5.6a1.6 1.6 0 1 1 0-3.2 1.6 1.6 0 0 1 0 3.2z"/></svg>
        <span>address (street address<br>suite number, city, state, zip</span>
      </li>
      <li>
        <svg viewBox="0 0 12 12"><path class="solid" d="M2.5 1h2l1 2.6-1.3 1a6.5 6.5 0 0 0 3.2 3.2l1-1.3L11 7.5v2c0 .8-.7 1.5-1.5 1.5A9 9 0 0 1 1 2.5C1 1.7 1.7 1 2.5 1z"/></svg>
        <span>0123 456 789</span>
      </li>
      <li>
        <svg viewBox="0 0 12 12"><rect x="3" y="0.8" width="6" height="10.4" rx="1"/><line x1="5.2" y1="9.3" x2="6.8" y2="9.3"/></svg>
        <span>0123 456 789</span>
      </li>
      <li>
        <svg viewBox="0 0 12 12"><rect x="0.8" y="2.2" width="10.4" height="7.6" rx="0.8"/><polyline points="1,2.6 6,6.6 11,2.6"/></svg>
        <span>youremail@postbay.net</span>
      </li>
      <li>
        <svg viewBox="0 0 12 12"><circle cx="6" cy="6" r="5"/><ellipse cx="6" cy="6" rx="2.2" ry="5"/><line x1="1" y1="6" x2="11" y2="6"/></svg>
        <span>www.yoursite-drift.net</span>
      </li>
    </ul>

    <div class="holder">
      <p class="holder-name">your name</p>
      <p class="holder-role">designation</p>
    </div>
  </section>

</main>
</body>
</html>
```